Storm Restoration Contractor needs a professional business card design

Looking for a professional business card design. Not looking for your cheapo MS Word standard ones that are readily available. Dont want it to be cookie cutter look like ones readily available online. We just recently changed our logo and want to freshen up all our documents. Our company handles restoring a property back to a pre-loss condition after a storm damages it. For example, wind, hail, flood, fire losses.

Target Market(s)

Property Owners, Homeowners, Property Owners, Commercial Property Owners, Property Management Companies, Hail and Wind Damaged Properties

Industry/Entity Type

Construction Company

Contact Information for Business Card

Brightline Facades
847-555-0193
847-555-0147 fax
www.brightlinefacades.example
info@brightlinefacades.example

Requirements
Must have
• Clean, Professional, fresh look
• Storm Restoration, Roofing, Siding, Windows
Nice to have
• If there is a way to incorporate storms that may be cool.

```html
<!DOCTYPE html>
<html lang="en">
<head>
<meta charset="utf-8">
<title>Brightline Facades – Business Card</title>
<link href="https://fonts.googleapis.com/css2?family=Arimo:wght@400;700&display=swap" rel="stylesheet">
<style>
  :root {
    --stage: #2a2a2c;
    --card-white: #f7f7f7;
    --brand-blue: #1f86d6;
    --brand-blue-dark: #1568b0;
    --slate: #2c2e33;
    --slate-text: #4a4d54;
    --ink-light: #e6e8eb;
    --ink-muted: #b9bdc3;
  }
  * { box-sizing: border-box; margin: 0; padding: 0; }
  html, body { width: 1200px; height: 997px; overflow: hidden; }
  body {
    background: var(--stage);
    font-family: "Arimo", Arial, sans-serif;
    position: relative;
  }
  .card {
    position: absolute;
    left: 300px;
    width: 600px;
    height: 343px;
    border-radius: 18px;
    overflow: hidden;
    background: var(--card-white);
    box-shadow: 0 18px 40px rgba(0,0,0,.45);
  }
  .card--front { top: 110px; }
  .card--back  { top: 543px; }

  .edge-band {
    position: absolute;
    top: 0; bottom: 0;
    width: 22px;
    background: linear-gradient(90deg, var(--brand-blue-dark), var(--brand-blue));
  }
  .edge-band--left  { left: 0; }
  .edge-band--right { right: 0; }

  .brand-block {
    position: absolute;
    display: flex;
    flex-direction: column;
    align-items: center;
    gap: 14px;
  }
  .brand {
    display: flex;
    align-items: center;
    gap: 14px;
  }
  .brand__dot {
    width: 44px; height: 44px;
    border-radius: 50%;
    background: var(--brand-blue);
    flex: none;
  }
  .brand__name {
    font-weight: 700;
    font-size: 30px;
    line-height: 1.05;
    color: var(--brand-blue);
    letter-spacing: .5px;
    text-transform: uppercase;
    white-space: nowrap;
  }
  .services {
    font-size: 12px;
    letter-spacing: .6px;
    color: var(--slate-text);
    text-transform: uppercase;
    white-space: nowrap;
  }
  .card--front .brand-block { left: 50%; top: 50%; transform: translate(-50%, -50%); }

  .card--back .brand-block {
    left: 22px; width: 306px;
    top: 50%; transform: translateY(-50%);
    gap: 12px;
  }
  .card--back .brand { gap: 12px; }
  .card--back .brand__dot { width: 40px; height: 40px; }
  .card--back .brand__name { font-size: 24px; }
  .card--back .services { font-size: 10px; letter-spacing: .3px; }

  .info-panel {
    position: absolute;
    top: 0; bottom: 0; right: 0;
    width: 272px;
    background: var(--slate);
    border-left: 9px solid var(--brand-blue);
    padding: 64px 28px 0 24px;
    color: var(--ink-light);
  }
  .info-panel .edge-band--right { width: 18px; }
  .person__name {
    font-weight: 700;
    font-size: 15px;
    color: var(--brand-blue);
    text-transform: uppercase;
    letter-spacing: .4px;
    display: inline-block;
    border-bottom: 2px solid var(--brand-blue);
    padding-bottom: 2px;
  }
  .person__role { font-size: 11px; color: var(--ink-muted); margin-top: 3px; }
  .address { font-size: 12px; line-height: 1.4; margin-top: 8px; }
  .contact-list { list-style: none; margin-top: 12px; font-size: 12px; }
  .contact-list li { display: flex; align-items: center; gap: 8px; margin-bottom: 8px; white-space: nowrap; }
  .contact-list svg { width: 12px; height: 12px; fill: var(--brand-blue); flex: none; }
  .contact-list .web { color: var(--brand-blue); font-weight: 700; }
</style>
</head>
<body>

<section class="card card--front" aria-label="Business card front">
  <div class="edge-band edge-band--left"></div>
  <div class="edge-band edge-band--right"></div>
  <div class="brand-block">
    <div class="brand">
      <span class="brand__dot"></span>
      <span class="brand__name">Brightline Facades</span>
    </div>
    <p class="services">Storm Restoration · Roofing · Siding · Windows</p>
  </div>
</section>

<section class="card card--back" aria-label="Business card back">
  <div class="edge-band edge-band--left"></div>
  <div class="brand-block">
    <div class="brand">
      <span class="brand__dot"></span>
      <span class="brand__name">Brightline<br>Facades</span>
    </div>
    <p class="services">Storm Restoration · Roofing · Siding · Windows</p>
  </div>
  <div class="info-panel">
    <div class="edge-band edge-band--right"></div>
    <p class="person__name">Marcus Hale</p>
    <p class="person__role">Director</p>
    <p class="address">118 Linden Court #402<br>Fairview, MD 20810</p>
    <ul class="contact-list">
      <li>
        <svg viewBox="0 0 24 24"><path d="M6.6 10.8a15 15 0 0 0 6.6 6.6l2.2-2.2a1 1 0 0 1 1-.25 11.4 11.4 0 0 0 3.6.57 1 1 0 0 1 1 1V20a1 1 0 0 1-1 1A17 17 0 0 1 3 4a1 1 0 0 1 1-1h3.5a1 1 0 0 1 1 1c0 1.250.2 2.45.57 3.57a1 1 0 0 1-.25 1z"/></svg>
        <span>847-555-0193</span>
      </li>
      <li>
        <svg viewBox="0 0 24 24"><path d="M6 3h10v5H6zM4 9h16a2 2 0 0 1 2 2v7h-4v3H6v-3H2v-7a2 2 0 0 1 2-2zm4 7v3h8v-3z"/></svg>
        <span>847-555-0147</span>
      </li>
      <li>
        <svg viewBox="0 0 24 24"><path d="M2 5h20v14H2zm2 2v.5l8 5 8-5V7zm0 3v7h16v-7l-8 5z"/></svg>
        <span>info@brightlinefacades.example</span>
      </li>
      <li>
        <svg viewBox="0 0 24 24"><path d="M12 2a7 7 0 0 1 7 7c0 5-7 13-7 13S5 14 5 9a7 7 0 0 1 7-7zm0 4.5A2.5 2.5 0 1 0 12 11.5 2.5 2.5 0 0 0 12 6.5z"/></svg>
        <span class="web">www.brightlinefacades.example</span>
      </li>
    </ul>
  </div>
</section>

</body>
</html>
```